Health and Wellness Company Business Card

I need a business card design that is clean and uses modern minimalist style. The design should incorporate our logo (see attached). I would also like to use embossing on the cards so that they also have a great feel. I am open to the card using one or more colors, and these do not have to correspond to the colors in the concept paper. The card can either be one-sided or use both sides of the card.The logo uses the Avenir font.

I will need the file designed in Adobe CS and compatible with CS5.5 (Illustrator preferable) and I'll need the working file (for example: .ai) once the project is complete so that I can change the names/contact info/etc for each variation of the card.

This needs to be a memorable card for the recipient. They should think: "This is a great business card" either because of its simplicity or embossing effects or use of color.

Target Market(s)

The audience for our company has two main groups: people who pay for healthcare (insurers, companies, researcher companies) and people with chronic health conditions who are the consumers of our services and resources.

Industry/Entity Type

Business

Requirements
Must have
• Essential components of the card include: Company logo, contact Name (Mark Tolley), phone number (5808127346), email address (mtolley@brenquora.com), slogan/tagline that consists of ~30-40 characters (Use Lorem Ipsum)
Nice to have
• These fall just slightly short of "must have" to allow for design flexibility: Embossing or spot varnish effects and a splash of color
Should not have
• Designs with these components will not be successful: flashy or showy designs that are not professional in appearance, and lots of different colors

```html
<!DOCTYPE html>
<html lang="en">
<head>
<meta charset="utf-8">
<title>Brenquora Business Card</title>
<link href="https://fonts.googleapis.com/css2?family=Nunito+Sans:ital,wght@0,400;0,600;1,400&display=swap" rel="stylesheet">
<style>
  :root {
    --backdrop: #ebebed;
    --card-white: #ffffff;
    --lilac-light: #a3a0ae;
    --lilac-dark: #777487;
    --ink: #8a8795;
    --ink-soft: #75727f;
    --rule: #c9c7cf;
    --paper: #ffffff;
  }
  * { margin: 0; padding: 0; box-sizing: border-box; }
  html, body {
    width: 1200px;
    height: 720px;
    overflow: hidden;
    background: var(--backdrop);
    font-family: "Nunito Sans", sans-serif;
  }
  .canvas {
    position: relative;
    width: 1200px;
    height: 720px;
  }
  .card {
    position: absolute;
    top: 241px;
    width: 420px;
    height: 240px;
    border-radius: 18px;
    overflow: hidden;
  }
  .card--front {
    left: 147px;
    background: linear-gradient(200deg, var(--lilac-light) 0%, var(--lilac-dark) 100%);
  }
  .card--back {
    left: 633px;
    background: var(--card-white);
  }

  /* front */
  .front-brand {
    position: absolute;
    left: 30px;
    top: 70px;
    display: flex;
    align-items: center;
    gap: 12px;
  }
  .front-brand__square {
    width: 34px;
    height: 34px;
    background: var(--paper);
    border-radius: 4px;
  }
  .front-brand__name {
    color: var(--paper);
    font-weight: 600;
    font-size: 30px;
    letter-spacing: 0.18em;
    text-transform: uppercase;
  }
  .tagline {
    position: absolute;
    right: 40px;
    top: 204px;
    color: var(--paper);
    font-style: italic;
    font-size: 12px;
    letter-spacing: 0.01em;
  }

  /* back */
  .brand {
    position: absolute;
    left: 0;
    right: 0;
    top: 30px;
    display: flex;
    flex-direction: column;
    align-items: center;
    gap: 16px;
  }
  .brand__square {
    width: 52px;
    height: 52px;
    background: var(--ink);
    border-radius: 6px;
  }
  .brand__name {
    color: var(--ink);
    font-weight: 600;
    font-size: 19px;
    letter-spacing: 0.38em;
    padding-left: 0.38em;
    text-transform: uppercase;
  }
  .person-name {
    position: absolute;
    left: 31px;
    top: 169px;
    color: var(--ink);
    font-weight: 600;
    font-size: 13.5px;
    letter-spacing: 0.02em;
    text-transform: uppercase;
  }
  .divider {
    position: absolute;
    left: 216px;
    top: 183px;
    width: 1px;
    height: 27px;
    background: var(--rule);
  }
  .contact {
    position: absolute;
    right: 45px;
    top: 172px;
    list-style: none;
    text-align: right;
    color: var(--ink-soft);
    font-size: 11.5px;
    line-height: 15.5px;
  }
</style>
</head>
<body>
  <main class="canvas">
    <section class="card card--front" aria-label="Card front">
      <div class="front-brand">
        <span class="front-brand__square"></span>
        <span class="front-brand__name">brenquora</span>
      </div>
      <p class="tagline">The sample tagline goes here......</p>
    </section>

    <section class="card card--back" aria-label="Card back">
      <div class="brand">
        <span class="brand__square"></span>
        <span class="brand__name">brenquora</span>
      </div>
      <p class="person-name">Mark Tolley</p>
      <span class="divider"></span>
      <ul class="contact">
        <li>5808127346</li>
        <li>mtolley@brenquora.com</li>
        <li>www.brenquora.com</li>
      </ul>
    </section>
  </main>
</body>
</html>
```